www.vandrik.com Sales/Order Page ReDesign

We need a new and amazing design for our sales/order page to attract more costumers and new houses for our portal.

Here is the existing page with the current design: https://www.vandrik.com/sales

We are proud owners of www.hyttetun.no and www.vandrik.com and we want more holiday home owners to join our page so that we can rent out their holiday homes and increase the number of houses on our portal.

To get more homeowners we need a sales page that can sell our products the best way possible. Therefore we want you too blow us away with a fresh, modern, easy understandable and stylish new sales/order page.

The only restrictions we give when it comes to design is that it needs to fit the existing design of our portals, the top and footer are set. Beside that we are open for everything as long as it at once give the customers impression that this is a good, professional page were they just have to put out their houses.

When it comes to content I have added two documents who include the content to put in here and some guidelines on how to organize the page. Please be creative and add necessary graphics, symbols, background pictures and what ever necessary to make this page look professional and appealing to new costumers.

Looking forward to what suggestions we are given.
Updates

We just want to inform that we have updated our brief with a much more concrete description of what content to add on the sale page, and who to structure the content on the page. Hope this helps to make suggestions easier. Looking forward to receive some good contributions.

We would just like to make sure that everyone have understood that we are not asking for a new design suggestion to our portal in general. We are only asking for a redesign of our sales/order page you find here www.vandrik.com/sales. We have to day received some designs for our front page and the design it self was good, but that's not what we are asking for this time and don't want you to use time of something we don't need at the moment. We are looking forward too se some good suggestions.

Project Deadline Extended
Reason: Hello. Thanks for all the great contributions we have been given so fare. We haven't been able to respond to all design and are therefore extending the deadline so that we are able to respond to the designs we have been giver and to gov time to make final changes.

Project Deadline Extended
Reason: We are extending the deadline to give designers time to give new suggestion based on our latest feedback today.

Project Deadline Extended
Reason: Extended so we can receive last design changes.

Target Market(s)

This is a presentation page where we present our product agains new home owner who we what to choose listing there property on or site.

Industry/Entity Type

Sales

Requirements
Must have
• A modern design who calms the costumer down and help them in deciding to chose us, and for them to choose us they need to trust and believe in us. Therefore your main task is to create a page that effectively informs about our product, gets the visitors attentions and make them trust us.
Nice to have
• Examples of good competitors and good order pages we like:

http://www.stayplume.com/info/lyp?icid=IL___O_Text___top_nav_link
https://www.nestorly.com/rooms/new
https://www.quince.com/tablo/compare/
http://www.lodgewick.com/host
Should not have
• - Bad design :-). With bad design we mean design that looks like it's made in 2 seconds by a little child.

```html
<!DOCTYPE html>
<html lang="en">
<head>
<meta charset="utf-8">
<title>Vandrik – List your property</title>
<link rel="stylesheet" href="https://fonts.googleapis.com/css2?family=Roboto:wght@300;400;500&family=Shadows+Into+Light&display=swap">
<style>
:root{
  --page:#f3f3f3;
  --text:#555;
  --text-soft:#777;
  --line:#dcdcdc;
  --field-border:#cfcfcf;
  --orange:#f5a01a;
  --orange-dark:#e08a06;
  --green:#6dbf3e;
  --green-dark:#55a52b;
  --blue:#3bb5de;
  --blue-dark:#259fc8;
  --brand:#1f7fc4;
  --tick:#c9c9c9;
  --footer:#0a86d8;
  --footer-dark:#0777c4;
  --white:#fff;
}
*{box-sizing:border-box;margin:0;padding:0}
html,body{width:720px;height:1200px;overflow:hidden}
body{background:var(--page);font-family:"Roboto",Arial,sans-serif;color:var(--text);position:relative}
.abs{position:absolute}

.intro{left:0;top:4px;width:720px;text-align:center;font-weight:300;font-size:15.5px;line-height:17px;color:#4a4a4a}

.contact-form .label{font-size:10px;color:#444}
.field{background:var(--white);border:1px solid var(--field-border);border-radius:3px;font-size:10px;color:#aaa;padding:3px 8px;height:20px}
.area{background:var(--white);border:1px solid var(--field-border);border-radius:3px}
.vdivider{left:328px;top:60px;width:1px;height:102px;background:var(--line)}
.rule{left:77px;width:571px;height:1px;background:var(--line)}

.plan{top:206px;width:185px;height:426px;background:var(--white);box-shadow:0 1px 3px rgba(0,0,0,.18)}
.plan-head{height:76px;color:var(--white);position:relative}
.plan-head .price{position:absolute;left:10px;top:10px;font-size:25px;font-weight:500}
.plan-head .rate{position:absolute;right:10px;top:10px;font-size:25px;font-weight:400}
.plan-head .sub{position:absolute;bottom:16px;font-size:9.5px}
.plan-head .sub.l{left:10px}.plan-head .sub.r{right:10px}
.plan.orange .plan-head{background:linear-gradient(#f7ab2c,var(--orange-dark))}
.plan.green .plan-head{background:linear-gradient(#79c94a,var(--green-dark))}
.plan.blue .plan-head{background:linear-gradient(#49c0e6,var(--blue-dark))}
.features{list-style:none;padding:10px 10px 0 12px}
.features li{position:relative;padding-left:20px;font-size:10px;line-height:12.5px;color:#555;margin-bottom:10px}
.features li::before{content:"";position:absolute;left:0;top:0;width:12px;height:12px;border-radius:50%;background:var(--tick)}
.features li::after{content:"";position:absolute;left:4px;top:2px;width:3px;height:6px;border:solid var(--white);border-width:0 1.6px 1.6px 0;transform:rotate(45deg)}
.partner{display:flex;align-items:center;gap:6px;margin:4px 0 14px 30px;font-size:15px;font-weight:500;color:var(--brand)}
.partner .mark{width:14px;height:14px;background:var(--brand)}
.partner.grey{color:#6d8aa0}.partner.grey .mark{background:#6d8aa0;border-radius:50%}
.upgrade{text-align:center;font-size:10px;color:#444;margin-top:2px}
.picker{margin:6px auto 0;width:104px;height:20px;border:1px solid var(--field-border);border-radius:3px;font-size:9.5px;color:#888;padding:3px 8px;position:relative}
.picker::after{content:"";position:absolute;right:7px;top:7px;border:4px solid transparent;border-top:5px solid #333}
.btn{position:absolute;color:var(--white);font-size:11.5px;text-align:center;border-radius:2px;text-transform:uppercase;letter-spacing:.2px}
.btn.orange{background:linear-gradient(#f8ad2e,var(--orange-dark));border:1px solid #d08008}
.btn.green{background:linear-gradient(#7dcc4e,var(--green-dark));border:1px solid #4b9a24}
.btn.blue{background:linear-gradient(#4ec3e8,var(--blue-dark));border:1px solid #1f94bb}
.plan .btn{left:41px;top:387px;width:103px;height:26px;line-height:24px}

.note{left:82px;top:639px;font-size:8.5px;color:#555}
.cta-text{left:0;width:720px;top:682px;text-align:center;font-size:14.4px;font-weight:300;color:#444}
.cta-glow{left:150px;top:742px;width:420px;height:18px;border-radius:50%;background:radial-gradient(ellipse at center,rgba(0,0,0,.09),rgba(0,0,0,0) 70%)}

.help{left:77px;top:784px;width:571px;height:86px;background:linear-gradient(90deg,#fff 60%,#fbfbe8);box-shadow:0 1px 3px rgba(0,0,0,.18)}
.help-icon{left:8px;top:15px;width:56px;height:56px;border-radius:50%;background:radial-gradient(circle,#f4f4f4 34%,#e24a3c 36%,#c9352a 72%)}
.help-title{left:72px;top:8px;font-family:"Shadows Into Light",cursive;font-size:21px;line-height:24px;color:#8a8a8a;white-space:nowrap}
.help-copy{left:74px;top:37px;width:172px;font-size:10px;line-height:12px;color:#333}
.help-arrow{left:196px;top:48px}
.help .label{font-size:10px;color:#444}
.help .field{width:163px;height:21px}
.soon{left:500px;top:14px;width:64px;font-family:"Shadows Into Light",cursive;font-size:12.5px;line-height:18px;color:#999;text-align:center}
.personal{left:0;width:720px;top:887px;text-align:center;font-size:10px;line-height:12px;color:#555}

.calc-icon{left:88px;top:960px;width:22px;height:34px;border-radius:2px;background:#b9b9b9}
.calc-text{left:124px;top:962px;font-size:12.5px;line-height:16px;color:#555;font-weight:300}
.calc-btn{left:552px;top:966px;width:96px;height:25px;line-height:23px;font-size:12px}

.footer{left:0;top:1021px;width:720px;height:179px;background:var(--footer);color:var(--white)}
.fcol{position:absolute;top:30px;font-size:8.4px;line-height:12.5px}
.fcol h3{font-size:9px;font-weight:500;margin-bottom:3px}
.fcol ul{list-style:none}
.fcol li{position:relative;padding-left:14px}
.fcol li::before{content:"";position:absolute;left:0;top:2.5px;width:8px;height:8px;border-radius:50%;background:var(--white)}
.fcol li::after{content:"";position:absolute;left:2px;top:5px;border:2px solid transparent;border-left:3px solid var(--footer)}
.fcol.plain p{padding-left:14px}
.fsep{position:absolute;top:0;width:14px;height:179px;background:linear-gradient(90deg,rgba(255,255,255,0),rgba(255,255,255,.12),rgba(255,255,255,0))}
.map{left:142px;top:29px;width:132px;height:82px;border-radius:40% 45% 35% 40%;background:radial-gradient(ellipse,rgba(255,255,255,.95),rgba(255,255,255,.75))}
</style>
</head>
<body>

<p class="abs intro">We want to contact you to find the best way managing your portfolio<br>of properties type in your contact details and we will contact you as soon as possible</p>

<section class="contact-form">
  <span class="abs label" style="left:78px;top:66px">First Name</span>
  <div class="abs field" style="left:160px;top:62px;width:148px">First name</div>
  <span class="abs label" style="left:78px;top:93px">Last Name</span>
  <div class="abs field" style="left:160px;top:89px;width:148px">Last name</div>
  <span class="abs label" style="left:78px;top:120px">E-mail</span>
  <div class="abs field" style="left:160px;top:115px;width:148px">abc@abc.com</div>
  <span class="abs label" style="left:78px;top:147px">Phone Number</span>
  <div class="abs field" style="left:160px;top:143px;width:148px">000-00-0000</div>
  <div class="abs vdivider"></div>
  <span class="abs label" style="left:344px;top:67px">How they want to be contacted</span>
  <div class="abs area" style="left:490px;top:62px;width:152px;height:46px"></div>
  <span class="abs label" style="left:344px;top:120px">When they want to be contacted</span>
  <div class="abs area" style="left:490px;top:115px;width:152px;height:47px"></div>
</section>

<div class="abs rule" style="top:188px"></div>

<article class="abs plan orange" style="left:77px">
  <div class="plan-head"><span class="price">€ 995</span><span class="rate">0%</span><span class="sub l">annually per booking</span><span class="sub r">per booking</span></div>
  <ul class="features">
    <li>Our professional team is there for you</li>
    <li>One upfront fee</li>
    <li>No limits or fee on bookings</li>
    <li>No limits or fee on bookings request</li>
    <li>Advertise your property for 12 months</li>
    <li>Include announcements on:</li>
  </ul>
  <div class="partner"><span class="mark"></span>Hyttetun.no</div>
  <div class="partner grey"><span class="mark"></span>Vandrik</div>
  <div class="partner"><span class="mark"></span>Tunlist</div>
  <div class="btn orange">Select</div>
</article>

<article class="abs plan green" style="left:270px">
  <div class="plan-head"><span class="price">€ 0</span><span class="rate">18%</span><span class="sub l">annually per booking</span><span class="sub r">per booking</span></div>
  <ul class="features">
    <li>Our professional team is there for you</li>
    <li>No listing fee</li>
    <li>No limits on bookings</li>
    <li>No limits or fee on bookings request</li>
    <li>You decide when to advertise and for how long</li>
    <li>Include announcements on:</li>
  </ul>
  <div class="partner"><span class="mark"></span>Hyttetun.no</div>
  <div class="partner grey"><span class="mark"></span>Vandrik</div>
  <p class="upgrade">Upgrade with Tunlist.no:</p>
  <div class="picker">60 days &nbsp;&nbsp; € 50</div>
  <div class="btn green">Select</div>
</article>

<article class="abs plan blue" style="left:464px">
  <div class="plan-head"><span class="price">€ 0</span><span class="rate">2%</span><span class="sub l">annually per booking</span><span class="sub r">per booking</span></div>
  <ul class="features">
    <li>You handle everything yourself</li>
    <li>No listing fee</li>
    <li>No limits on bookings</li>
    <li>No limits or fee &nbsp;on bookings request</li>
    <li>You decide when to advertise and for how long</li>
    <li>Include announcements on:</li>
  </ul>
  <div class="partner"><span class="mark"></span>Hyttetun.no</div>
  <div class="partner grey"><span class="mark"></span>Vandrik</div>
  <p class="upgrade">Upgrade with Tunlist.no:</p>
  <div class="picker">60 days &nbsp;&nbsp; € 50</div>
  <div class="btn blue">Select</div>
</article>

<p class="abs note">* Transaction fee for secure payment 4,5% comes in addition</p>

<div class="abs rule" style="top:668px"></div>

<p class="abs cta-text">You have not chosen to list any property with us, add a property</p>
<div class="btn green" style="left:300px;top:708px;width:127px;height:26px;line-height:24px">Add property</div>
<div class="abs cta-glow"></div>

<section class="abs help">
  <div class="abs help-icon" role="img" aria-label="Lifebuoy with envelope icon"></div>
  <span class="abs help-title">Help Required?</span>
  <p class="abs help-copy">If you want us to contact you too answer any question, Give us a few details...</p>
  <svg class="abs help-arrow" width="80" height="22" viewBox="0 0 80 22" aria-hidden="true"><path d="M2 20 Q40 22 74 6" fill="none" stroke="#aaa" stroke-width="1.2"/><path d="M68 4 L75 5 L72 11" fill="none" stroke="#aaa" stroke-width="1.2"/></svg>
  <span class="abs label" style="left:283px;top:11px">Name</span>
  <div class="abs field" style="left:325px;top:7px"></div>
  <span class="abs label" style="left:283px;top:37px">Email</span>
  <div class="abs field" style="left:325px;top:33px"></div>
  <span class="abs label" style="left:283px;top:63px">Phone</span>
  <div class="abs field" style="left:325px;top:60px"></div>
  <p class="abs soon">We will back soon...</p>
  <div class="btn green" style="left:500px;top:60px;width:65px;height:20px;line-height:18px;font-size:10.5px">Send</div>
</section>

<p class="abs personal">If you want personal guidelines we are more then willing to call you, type in your name<br>and number here and someone will contact you as soon as possible</p>

<svg class="abs calc-icon" viewBox="0 0 22 34" role="img" aria-label="Calculator icon"><rect x="3" y="3" width="16" height="8" fill="#e6e6e6"/><g fill="#e6e6e6"><rect x="3" y="14" width="4" height="4"/><rect x="9" y="14" width="4" height="4"/><rect x="15" y="14" width="4" height="4"/><rect x="3" y="20" width="4" height="4"/><rect x="9" y="20" width="4" height="4"/><rect x="15" y="20" width="4" height="4"/><rect x="3" y="26" width="4" height="4"/><rect x="9" y="26" width="4" height="4"/><rect x="15" y="26" width="4" height="4"/></g></svg>
<p class="abs calc-text">You now know that you are going to list your property, but are uncertain<br>which listing option is right for you? &nbsp;calculate what’s most profitable for you...</p>
<div class="btn orange calc-btn">Calculate</div>

<footer class="abs footer">
  <div class="fsep" style="left:282px"></div>
  <div class="fsep" style="left:384px"></div>
  <div class="fsep" style="left:516px"></div>
  <div class="abs map" role="img" aria-label="World map"></div>
  <div class="fcol" style="left:70px">
    <h3>Destinations</h3>
    <ul><li>Europe</li><li>North America</li><li>South America</li><li>Africa</li><li>Asia</li><li>Australia</li></ul>
  </div>
  <div class="fcol" style="left:300px">
    <h3>For tenants</h3>
    <ul><li>My page</li><li>Why Vandrik?</li><li>Help</li><li>Rental terms</li></ul>
  </div>
  <div class="fcol" style="left:402px">
    <h3>For house owners</h3>
    <ul><li>MyAdmin</li><li>Let us rent your house</li><li>Conditions</li></ul>
  </div>
  <div class="fcol plain" style="left:534px;top:28px">
    <h3>Contact us</h3>
    <p>Vandrik Holiday Rental</p><p>post@vandrik.com</p><p>+47 51 20 40 88</p><p>www.vandrik.com</p>
    <h3 style="margin-top:3px">Opening hours</h3>
    <p>Mon - Fri: 9.00 AM - 5.00 PM</p><p>Sat - Sun: Closed</p>
  </div>
</footer>

</body>
</html>
```